50's-style gig poster for a birthday bash

My wife was born in 1957 and is turning 57 next month. I'm throwing a surprise party for her, and thought it would be fun to have a 18x24 poster printed and framed for the event. Attached is a poster from a Rolf Tesker gig in 1957. I'd like something like this, with a tinted B&W head shot of my wife, with similar fonts and background color schemes. The copy will be GRETA at the top (where the name ROLF appears), with 57X57 under it, and the word Celebration where the word Quartet currently appears. The rest of the copy will be provided to you. Thanks for your interest and I look forward to working with you.

```html
<!DOCTYPE html>
<html lang="en">
<head>
<meta charset="utf-8">
<title>GRETA 57 x 57 Celebration</title>
<link rel="stylesheet" href="https://fonts.googleapis.com/css2?family=Montserrat:ital,wght@0,700;0,800;1,600&family=Lobster&family=Arvo:wght@700&family=Limelight&family=Courier+Prime:wght@700&display=swap">
<style>
  :root {
    --paper: #e9dab3;
    --cream: #f4ecd8;
    --blue: #23438f;
    --red: #e31e26;
    --ink: #231f1c;
    --shadow: #2a211b;
  }
  html, body {
    margin: 0;
    padding: 0;
    width: 900px;
    height: 1200px;
    overflow: hidden;
    background: var(--paper);
  }
  .poster {
    position: relative;
    width: 900px;
    height: 1200px;
    background: radial-gradient(ellipse at 50% 40%, #eee2c0 0%, var(--paper) 70%, #dcc99c 100%);
    overflow: hidden;
  }
  .stripes { position: absolute; left: 0; top: 0; }
  .headline {
    position: absolute;
    left: 96px;
    width: 712px;
    display: flex;
    justify-content: space-between;
    align-items: center;
    font-family: "Montserrat", sans-serif;
    font-weight: 800;
    color: var(--cream);
    text-shadow: 6px 6px 0 var(--shadow);
    line-height: 1;
  }
  .headline--name { top: 44px; font-size: 168px; }
  .headline--age { top: 180px; font-size: 168px; }
  .headline--age .times { font-size: 100px; padding-top: 40px; }
  .photo-frame {
    position: absolute;
    left: 124px;
    top: 368px;
    width: 300px;
    height: 398px;
    background: var(--ink);
    padding: 10px;
    box-sizing: border-box;
    transform: rotate(-3.6deg);
    box-shadow: 4px 5px 0 rgba(0,0,0,0.35);
  }
  .photo {
    width: 100%;
    height: 100%;
    background: radial-gradient(ellipse at 55% 40%, #b9b6b2 0%, #8a8581 45%, #4d4845 100%);
  }
  .celebration {
    position: absolute;
    left: 438px;
    top: 332px;
    font-family: "Lobster", cursive;
    font-size: 76px;
    color: var(--cream);
    text-shadow: 4px 4px 0 var(--shadow);
    transform: rotate(-5deg);
    margin: 0;
    line-height: 1;
  }
  .lineup {
    position: absolute;
    left: 440px;
    width: 330px;
    top: 440px;
    margin: 0;
    padding: 0;
    list-style: none;
    text-align: center;
    font-family: "Montserrat", sans-serif;
    font-weight: 700;
    font-size: 23px;
    line-height: 37px;
    color: #ffffff;
    text-shadow: 2px 2px 0 var(--shadow);
  }
  .lineup .lead { font-style: italic; font-weight: 600; font-size: 22px; }
  .date-badge { position: absolute; left: 480px; top: 719px; }
  .date-badge text { text-anchor: middle; }
  .badge-title { font-family: "Arvo", serif; font-weight: 700; font-size: 28px; fill: var(--blue); }
  .badge-date { font-family: "Montserrat", sans-serif; font-weight: 700; font-size: 17px; fill: var(--blue); }
  .also {
    position: absolute;
    left: 168px;
    top: 846px;
    padding: 4px 14px 5px;
    background: var(--cream);
    border: 2px solid var(--ink);
    font-family: "Montserrat", sans-serif;
    font-weight: 700;
    font-size: 25px;
    color: var(--blue);
    transform: rotate(-2deg);
    line-height: 1.2;
  }
  .guests {
    position: absolute;
    left: 0;
    width: 900px;
    top: 884px;
    text-align: center;
    font-family: "Lobster", cursive;
    font-size: 72px;
    color: var(--cream);
    text-shadow: 4px 4px 0 var(--shadow);
    margin: 0;
    line-height: 1.2;
  }
  .venue {
    position: absolute;
    left: 121px;
    top: 1002px;
    width: 662px;
    height: 112px;
    box-sizing: border-box;
    background: var(--cream);
    border: 3px solid var(--ink);
    text-align: center;
    padding-top: 8px;
  }
  .venue-name {
    font-family: "Limelight", serif;
    font-size: 60px;
    color: var(--ink);
    letter-spacing: 2px;
    line-height: 1;
  }
  .venue-address {
    font-family: "Courier Prime", monospace;
    font-weight: 700;
    font-size: 22px;
    color: var(--blue);
    margin-top: 8px;
    letter-spacing: 0.5px;
  }
</style>
</head>
<body>
<div class="poster">
  <svg class="stripes" width="900" height="1200" viewBox="0 0 900 1200" aria-hidden="true">
    <rect x="90" y="42" width="128" height="1116" fill="var(--blue)"/>
    <rect x="238" y="42" width="130" height="1116" fill="var(--red)"/>
    <rect x="385" y="42" width="130" height="1116" fill="var(--blue)"/>
    <rect x="532" y="42" width="130" height="1116" fill="var(--red)"/>
    <rect x="679" y="42" width="130" height="1116" fill="var(--blue)"/>
  </svg>

  <div class="headline headline--name"><span>G</span><span>R</span><span>E</span><span>T</span><span>A</span></div>
  <div class="headline headline--age"><span>5</span><span>7</span><span class="times">x</span><span>5</span><span>7</span></div>

  <div class="photo-frame">
    <div class="photo" role="img" aria-label="Tinted black and white head shot of Greta, smiling and looking up"></div>
  </div>

  <h1 class="celebration">Celebration</h1>

  <ul class="lineup">
    <li class="lead">Featuring:</li>
    <li>The Marlowes</li>
    <li>The Whitcombs</li>
    <li>The Pennell-Ashbys</li>
    <li>The Corvells</li>
    <li>The Tanseys</li>
    <li>The Brisards</li>
  </ul>

  <svg class="date-badge" width="246" height="140" viewBox="0 0 246 140">
    <ellipse cx="123" cy="70" rx="120" ry="67" fill="var(--cream)" stroke="var(--ink)" stroke-width="2"/>
    <text class="badge-title" x="123" y="52">One Night</text>
    <text class="badge-title" x="123" y="80">Only</text>
    <text class="badge-date" x="123" y="104">April 4, 2014</text>
    <text class="badge-date" x="123" y="125">6 PM</text>
  </svg>

  <div class="also">Also Appearing</div>
  <p class="guests">The Larks &amp; Ned Vollan</p>

  <div class="venue">
    <div class="venue-name">BISTRO MARCHAND</div>
    <div class="venue-address">418 Alder Street, Cedar Bluff, California</div>
  </div>
</div>
</body>
</html>
```